Web Instant Messenger Design Project

Hello,
The project consist of designing a web instant messenger interface. What we need is a Photoshop file that contains the design elements of this app. (windows, buttons , dropdowns etc)
notes:
- we are looking for the same look and feel as the now closed Tirvak.com
- the name of the app will be lurnbey.com , or similar.
- the application will be browser based, will cover 100% of the browser area.
- please don't make a "flat" background.
I attached 3 screen captures that shows the graphic elements we need :
img1: -
is the login "page" with username and password fields. There are also a connect & disconnect buttons + a register one
img2:
a) We have the classic friend list that shows who is online and their status. The friend list window can be moved and has 7
buttons (down:add friedn, delete friend, create group,change friend group and create conference / up: conference room list
and mass message buttons)
b) There is a conversation window that can be dragged. The conversation window will keep the private conversations and
conferences as a tab bar. Please note the key field area .
c) Mass Message window - here you can select the group and/or friends, write the message and hit send.
img3
a) on friend list window , when you click one of the down button a new , non movable window will appear. In this window you will have actions corresponding to the button you clicked : add/ delete friend , create conference , etc
b) public room window- is a drag-able window with the conferences you can join.
c)the conversation window with a conference selected. There is a invite buddy drop down, a list of participants and the conversations zone. On participants list there will be a kick and ban button.(not present in this capture)
Updates
When submitting a design please try to provide a mock of the "friend list window". Thank you and sorry if this info comes too late.
Industry/Entity Type
Group
Look and feel
Each slider illustrates characteristics of the customer's brand and the style your logo design should communicate.

```html
<!DOCTYPE html>
<html lang="en">
<head>
<meta charset="utf-8">
<title>lurnbey.com – Friend List</title>
<link rel="stylesheet" href="https://fonts.googleapis.com/css2?family=Cabin:wght@400;500;600&display=swap">
<style>
  :root {
    --bg-top-left: #e9b6f2;
    --bg-mid: #9b8bd8;
    --bg-top-right: #5f7fc4;
    --bg-bottom: #bcb6e6;
    --header-light: #b4d0ea;
    --header-dark: #5f93c4;
    --header-text: #ffffff;
    --panel-top: #f5f5f5;
    --panel-bottom: #e3e3e3;
    --button-fill: #a3bddb;
    --button-text: #ffffff;
    --label-text: #444444;
    --muted-text: #9a9a9a;
    --group-text: #4b48a6;
    --divider: #9a9a9a;
    --online: #36d93a;
  }
  html, body {
    margin: 0;
    padding: 0;
    width: 1200px;
    height: 1065px;
    overflow: hidden;
  }
  body {
    position: relative;
    font-family: "Cabin", sans-serif;
    background:
      radial-gradient(ellipse 700px 500px at 0 0, var(--bg-top-left), transparent 70%),
      radial-gradient(ellipse 600px 400px at 1200px 0, var(--bg-top-right), transparent 75%),
      linear-gradient(180deg, var(--bg-mid) 0%, var(--bg-bottom) 100%);
  }
  .backdrop-curves {
    position: absolute;
    inset: 0;
  }
  .friend-list {
    position: absolute;
    left: 436px;
    top: 154px;
    width: 338px;
    height: 759px;
    border-radius: 3px;
    overflow: hidden;
    background: linear-gradient(180deg, var(--panel-top), var(--panel-bottom));
    box-shadow: 0 4px 10px rgba(40, 30, 80, 0.45);
  }
  .window-header {
    height: 56px;
    background: linear-gradient(180deg, var(--header-light) 0%, var(--header-dark) 55%, var(--header-light) 100%);
    border-bottom: 1px solid #8aa8c6;
    display: flex;
    align-items: center;
    padding-left: 14px;
    gap: 8px;
  }
  .window-title {
    color: var(--header-text);
    font-size: 17px;
    font-weight: 600;
    text-shadow: 0 1px 1px rgba(0, 0, 0, 0.35);
  }
  .toolbar {
    display: flex;
    gap: 11px;
    padding: 10px 0 0 10px;
  }
  .tool-button {
    width: 57px;
    height: 34px;
    border: none;
    border-radius: 3px;
    background: var(--button-fill);
    color: var(--button-text);
    font-family: "Cabin", sans-serif;
    font-size: 17px;
    font-weight: 600;
  }
  .status-row {
    display: flex;
    align-items: center;
    padding: 10px 0 0 10px;
    height: 28px;
  }
  .status-label {
    width: 67px;
    font-size: 16px;
    font-weight: 500;
    color: var(--label-text);
  }
  .status-select {
    position: relative;
    width: 207px;
    height: 28px;
    box-sizing: border-box;
    border: 1px solid #666;
    border-radius: 4px;
    background: linear-gradient(180deg, #ffffff, #dcdcdc);
    font-size: 13px;
    line-height: 26px;
    padding-left: 10px;
    color: #111;
  }
  .status-select .select-arrow {
    position: absolute;
    right: 0;
    top: 0;
    width: 24px;
    height: 26px;
    background: linear-gradient(180deg, #9a9a9a, #6e6e6e);
    border-radius: 0 3px 3px 0;
  }
  .divider {
    margin-top: 11px;
    border-top: 1px dashed var(--divider);
  }
  .group-title {
    margin: 12px 0 0 10px;
    font-size: 21px;
    color: var(--group-text);
  }
  .buddy-list {
    list-style: none;
    margin: 4px 0 0 0;
    padding: 0;
  }
  .buddy {
    position: relative;
    height: 42px;
    display: flex;
    align-items: center;
    font-size: 16px;
    color: var(--muted-text);
  }
  .buddy-dot {
    position: absolute;
    left: 35px;
    width: 18px;
    height: 18px;
    border-radius: 50%;
    background: radial-gradient(circle at 45% 35%, #c8ffc0 0%, var(--online) 55%, #1f9a25 100%);
    box-shadow: 0 2px 2px rgba(0, 0, 0, 0.3);
  }
  .buddy-name { position: absolute; left: 77px; }
  .buddy-state { position: absolute; right: 32px; }
</style>
</head>
<body>
  <svg class="backdrop-curves" width="1200" height="1065" viewBox="0 0 1200 1065" aria-hidden="true">
    <path d="M0 230 Q400 200 760 330 Q1000 300 1200 230 L1200 0 L0 0 Z" fill="#ffffff" opacity="0.06"/>
    <path d="M780 340 Q1000 120 1200 60 L1200 120 Q980 200 800 420 Z" fill="#f2b6ea" opacity="0.35"/>
    <path d="M1040 900 Q1100 500 1200 200 L1200 260 Q1130 560 1070 900 Z" fill="#f2b6ea" opacity="0.3"/>
    <path d="M0 780 Q500 640 1200 800 L1200 1065 L0 1065 Z" fill="#d2ccf0" opacity="0.3"/>
  </svg>

  <section class="friend-list">
    <header class="window-header">
      <svg width="30" height="26" viewBox="0 0 30 26" aria-hidden="true">
        <circle cx="19" cy="8" r="6" fill="#3d3d3d"/>
        <path d="M8 25 Q9 14 19 14 Q29 14 30 25 Z" fill="#3d3d3d"/>
        <circle cx="10" cy="10" r="5.5" fill="#eaeaea"/>
        <path d="M0 25 Q1 16 10 16 Q19 16 20 25 Z" fill="#eaeaea"/>
      </svg>
      <span class="window-title">Friend List</span>
    </header>

    <div class="toolbar">
      <button class="tool-button">MM</button>
      <button class="tool-button">R</button>
    </div>

    <div class="status-row">
      <span class="status-label">Status</span>
      <div class="status-select">Online
        <span class="select-arrow">
          <svg width="24" height="26" viewBox="0 0 24 26" aria-hidden="true"><path d="M8 10 L16 10 L12 16 Z" fill="#fff"/></svg>
        </span>
      </div>
    </div>

    <div class="divider"></div>

    <h2 class="group-title">Buddies</h2>
    <ul class="buddy-list">
      <li class="buddy"><span class="buddy-dot"></span><span class="buddy-name">tavi</span><span class="buddy-state">Offline</span></li>
      <li class="buddy"><span class="buddy-dot"></span><span class="buddy-name">tavi</span><span class="buddy-state">Offline</span></li>
      <li class="buddy"><span class="buddy-dot"></span><span class="buddy-name">tavi</span><span class="buddy-state">Offline</span></li>
      <li class="buddy"><span class="buddy-dot"></span><span class="buddy-name">tavi</span><span class="buddy-state">Offline</span></li>
    </ul>
  </section>
</body>
</html>
```